Race car follow-up website needs web design

We are currently finalising a website which allows amateur and professional owners of race cars to track the running time of the car and all installed parts (drive shafts, gearbox etc.). The site is working for a technical point of view, but needs a nice design applied to it.

The website is made with Bootstrap 3.x and does not need a mobile skin. We target desktop and tablet users. This means that the delivered work should be easy to incorporate in the Bootstrap site that currently exists, from a technical point of view.

In attachment you can find all the screens that need skinning. If you think some stuff can be done better from a usability or design point of view (size of tables, placement of buttons etc.), do not hesitate to make a suggestion. We are open to positive criticism, and the current "base" design is not carved in stone. The colors currently used are basic Bootstrap so that can change too. There are no limits whatsoever, as long as the result looks good.

We have a big amount of racing/racecar/mechanic/pitbox related photo material that can be used, so do not hesitate to ask for material if needed.

The start page should be something along the lines of these sites:

https://plumvex.me/
http://quorvane.io/
https://teldrova.com/
http://www.mivostrel.com/

Or in words: a top navigation bar (as seen in the screenshots). A full-width image relevant to the content (racing related) with some text in overlay (A sort of slogan along the lines of "Let us track your parts" or "Parts tracking for you race or trackday car" ). Under that image there should then be a very high-level overview of what the website can be used for (In a few steps, with graphics/photos, schematics, showing driving the car, data transfer, management in the site.). This so the potential user can quickly see if it is of any interest to him/her.

Basically:

Drive --- Download data -- Get Alerted

each step should contain an "icon" representing what it is about, and a few lines of text explaining what is meant.

On that page (in the image part, or below the explanation) there should be 2 links (buttons). One leads to the pricing page, one to the registration page.

Of course this first page cannot be finalised until we give the complete details of the content, so please provide a high-level design and the person I work with will receive the detailed specs (the text for the different steps etc).

The other screens are (we think) self-explanatory. Please look at them in chronological order (they are prefixed 00 to 19)

There are screenshots of the manual. This page will also need to be styled (to match the rest of the site and to make the layout a bit more sexy). We will of course provide the original html file to this once the content needs to be finalised.

Besides the website, a mail template is required too. The site sends mails for:
- registration confirmation
- lost password
- alerts related to the car parts or the data files.

These mails should also have a professional looking skin (right now they are plain text)

Just to make things clear, if you think the base design we made is "crap", please suggest improvements (for instance, menu placement in the bottom, positioning of certain elements, tables that might be better off somewhere else, the car details on top that take too much screen real-estate etc. etc.). This site has been built by developers, not by designers. The only condition is that it should be technically possible in a reasonable amount of time using Bootstrap 3.x

Please provide the resources in such a way that a developer with web skills can directly implement them. So any slicing of graphics should be done by the designer. If you only provide us a good looking psd file we won't be able to do anything with that, unfortunately.

If you, as a designer, have a passion for sports cars, race cars, trackdays and/or GT car racing, this is of course a plus. The collaboration will be a lot easier if we speak the same "language".

Please provide at least a design of
- the start page
- the "car details" page
- one of the list modals
- one of the form modals

so we can at least know how the rest of the pages will look

The name is Pitlane Ledger.

Some pictures that can be used:

https://www.snapvelo.com/photos/58310472@K04/20581937466/
https://www.snapvelo.com/photos/58310472@K04/4815209367/
https://www.snapvelo.com/photos/58310472@K04/4812766058/
https://www.snapvelo.com/photos/58310472@K04/4801533729/
https://www.snapvelo.com/photos/58310472@K04/4763921850/
https://www.snapvelo.com/photos/58310472@K04/4706418592/
https://www.snapvelo.com/photos/58310472@K04/4594071683/
https://www.snapvelo.com/photos/58310472@K04/4361829074/
https://www.snapvelo.com/photos/58310472@K04/3958316247/
https://www.snapvelo.com/photos/58310472@K04/3927140568/
https://www.snapvelo.com/photos/58310472@K04/3915762839/
https://www.snapvelo.com/photos/58310472@K04/3915764901/
https://www.snapvelo.com/photos/58310472@K04/3890417352/
https://www.snapvelo.com/photos/58310472@K04/3885093716/
https://www.snapvelo.com/photos/58310472@K04/3885097284/
https://www.snapvelo.com/photos/58310472@K04/2081359647/
https://www.snapvelo.com/photos/58310472@K04/2398640513/
https://www.snapvelo.com/photos/58310472@K04/2486075129/
https://www.snapvelo.com/photos/58310472@K04/2323149876/
https://www.snapvelo.com/photos/58310472@K04/2323154902/

Basically you take whatever you want from this guy’s photo stream:
https://www.snapvelo.com/photos/58310472@K04/

I know him personally so there should be no copyright issues.

Most users of the site will run so called "GT" cars (Valdorni, Castruzzo etc.), so please refrain from using (or referencing) open wheelers, F1, LMP etc.

There is a logo contest too: http://gigs.pixelbazaar.com/gig.aspx?id=837461

I just updated the brief with some more info and images you can use.

I have updated the brief. This is added: for the first screen, the schematics are explained in a bit more detail: Basically: Drive ---> Download data --> Get Alerted each step should contain an "icon" representing what it is about, and a few lines of text explaining what is meant.

Dear designers, As we have received numerous remarks about our contest from you and your colleagues we have contacted PixelBazaar to solve the situation. This contest will be split into two different contests. One logo design contest for $400 and one website design contest for the $1480. Everyone who has submitted logos can of course participate with those logos in the logo design contest (there are a few that we like, which have been submitted). We are very sorry for the inconvenience we might have caused, and if you want to redraw your designs already submitted because of this we will fully understand this, but we hope this decision will make things clearer for everyone participating. As soon as matters are changed we will send you all a new message with the updated information. Thanks for your understanding. Morlek BVBA

The logo contest has been created: http://gigs.pixelbazaar.com/gig.aspx?id=837461

Reason: Because of the split in webdesign / logo the deadline has been extended so non-logo webdesigners can participate too. Logo project: http://gigs.pixelbazaar.com/gig.aspx?id=837461

The pricing page has been added in the screenshots section

Trackday enthousiasts, race car owners, race teams.

• No video
No huge "footer" with a lot of links to navigate the site, since there will be very litte content.
No references to non-GT type cars (so no F1, no Series Quelmont, no LMP1/LMP2) or street cars.

```html
<!DOCTYPE html>
<html lang="en">
<head>
<meta charset="utf-8">
<title>Pitlane Ledger – Let us track your parts</title>
<link rel="stylesheet" href="https://fonts.googleapis.com/css2?family=Open+Sans:wght@400;600;700;800&display=swap">
<style>
  :root {
    --red: #b5121b;
    --red-dark: #8e0d14;
    --ink: #1d1d1d;
    --text: #444;
    --muted: #9a9a9a;
    --white: #fff;
    --line: #e6e6e6;
  }
  * { box-sizing: border-box; margin: 0; padding: 0; }
  html, body { width: 764px; height: 1200px; overflow: hidden; background: var(--white); }
  body { position: relative; font-family: "Open Sans", Arial, sans-serif; color: var(--text); }
  a { color: inherit; text-decoration: none; }

  .brand { display: flex; align-items: center; gap: 6px; font-weight: 800; color: var(--ink); text-transform: uppercase; letter-spacing: .5px; }
  .brand-dot { width: 12px; height: 12px; border-radius: 50%; background: var(--red); flex: none; }

  /* header */
  .site-header { position: absolute; top: 0; left: 0; width: 764px; height: 50px; background: var(--white); box-shadow: 0 2px 4px rgba(0,0,0,.15); z-index: 2; }
  .site-header .brand { position: absolute; left: 67px; top: 14px; font-size: 17px; }
  .nav-signup { position: absolute; left: 594px; top: 17px; font-size: 9px; color: var(--muted); letter-spacing: .3px; }
  .nav-login { position: absolute; left: 639px; top: 11px; width: 62px; height: 24px; border: 1px solid var(--line); border-bottom: 2px solid var(--red); border-radius: 2px; font-size: 9px; font-weight: 700; color: var(--ink); display: flex; align-items: center; justify-content: center; }

  /* hero */
  .hero { position: absolute; top: 50px; left: 0; width: 764px; height: 294px; background: linear-gradient(100deg, #8a8d90 0%, #6e7276 35%, #3b3d40 60%, #1a1a1c 75%, #7d8074 100%); }
  .hero-title { position: absolute; left: 63px; top: 60px; font-size: 27px; line-height: 33px; font-weight: 800; color: var(--white); text-shadow: 0 1px 3px rgba(0,0,0,.4); }
  .hero-lead { position: absolute; left: 63px; top: 127px; width: 210px; font-size: 12.5px; line-height: 15px; font-weight: 700; color: var(--white); text-shadow: 0 1px 3px rgba(0,0,0,.4); }
  .btn { position: absolute; height: 23px; font-size: 9.5px; font-weight: 700; text-transform: uppercase; display: flex; align-items: center; justify-content: center; border-radius: 2px; box-shadow: 0 2px 2px rgba(0,0,0,.25); }
  .btn-light { background: var(--white); color: var(--red); border-bottom: 2px solid var(--red); }
  .btn-red { background: var(--red); color: var(--white); border-bottom: 2px solid var(--red-dark); }
  .hero .btn-pricing { left: 63px; top: 201px; width: 62px; }
  .hero .btn-register { left: 131px; top: 201px; width: 104px; }
  .hero-dots { position: absolute; left: 355px; top: 276px; display: flex; gap: 3px; }
  .hero-dots span { width: 9px; height: 8px; background: rgba(255,255,255,.55); }
  .hero-dots span.active { background: var(--red); }

  /* intro */
  .intro { position: absolute; top: 344px; left: 0; width: 764px; height: 152px; }
  .intro-heading { position: absolute; left: 90px; top: 56px; width: 200px; font-size: 12px; font-weight: 600; color: var(--red); line-height: 18px; }
  .intro-heading .brand { font-size: 17px; }
  .intro-divider { position: absolute; left: 302px; top: 22px; width: 4px; height: 110px; background: linear-gradient(90deg, rgba(0,0,0,.12), rgba(0,0,0,0)); }
  .intro-text { position: absolute; left: 336px; top: 53px; width: 342px; font-size: 7.4px; line-height: 9.1px; }

  /* features */
  .feature { position: absolute; left: 0; width: 764px; height: 201px; border-top: 1px solid var(--line); overflow: hidden; }
  .feature-photo { position: absolute; top: 0; height: 100%; }
  .feature-title { position: absolute; font-size: 17px; font-weight: 600; color: var(--red); display: flex; align-items: center; gap: 9px; text-transform: uppercase; }
  .feature-title .ring { width: 12px; height: 12px; border: 1.5px solid var(--red); border-radius: 50%; }
  .feature-text { position: absolute; font-size: 7.4px; line-height: 9.1px; }
  .feature .btn { width: 104px; }

  .feature-car { top: 496px; }
  .feature-car .feature-photo { left: 0; width: 440px; background: linear-gradient(90deg, rgba(255,255,255,0) 55%, #fff 98%), linear-gradient(180deg, #d9dde2 0%, #b8bcc0 30%, #8d6f70 55%, #6b6d70 75%, #a6a8a8 100%); }
  .feature-car .feature-title { right: 98px; top: 40px; }
  .feature-car .feature-text { right: 120px; top: 70px; width: 300px; text-align: right; }
  .feature-car .btn { left: 541px; top: 134px; }

  .feature-data { top: 697px; }
  .feature-data .feature-photo { right: 0; width: 434px; background: linear-gradient(270deg, rgba(255,255,255,0) 55%, #fff 98%), linear-gradient(180deg, #c7c9c6 0%, #8c8f8f 30%, #4d4f52 55%, #2a2a2c 75%, #b3b4b2 100%); }
  .feature-data .feature-title { left: 97px; top: 46px; }
  .feature-data .feature-text { left: 120px; top: 76px; width: 262px; }
  .feature-data .btn { left: 119px; top: 124px; }

  .feature-management { top: 898px; height: 202px; }
  .feature-management .feature-photo { left: 0; width: 440px; background: linear-gradient(90deg, rgba(255,255,255,0) 55%, #fff 98%), linear-gradient(180deg, #9ea3a6 0%, #6a6d70 35%, #3a3a3d 60%, #7b2a2c 78%, #5a5c5e 100%); }
  .feature-management .feature-title { right: 98px; top: 48px; }
  .feature-management .feature-text { right: 120px; top: 79px; width: 268px; text-align: right; }
  .feature-management .btn { left: 539px; top: 126px; }

  /* footer */
  .site-footer { position: absolute; top: 1100px; left: 0; width: 764px; height: 100px; border-top: 1px solid var(--line); text-align: center; }
  .site-footer .brand { position: absolute; left: 0; right: 0; top: 20px; justify-content: center; font-size: 11px; }
  .social { position: absolute; left: 0; right: 0; top: 48px; display: flex; justify-content: center; gap: 18px; font-size: 6px; }
  .social-item { display: flex; align-items: center; gap: 2px; }
  .social-btn { background: #5b6f9e; color: var(--white); font-weight: 700; padding: 1px 5px; border-radius: 2px; }
  .social-btn.follow { background: #eef1f4; color: #333; border: 1px solid #c9cdd2; }
  .social-count { border: 1px solid #c9cdd2; padding: 0 3px; color: #555; }
  .footer-nav { position: absolute; left: 0; right: 0; top: 65px; display: flex; justify-content: center; gap: 11px; font-size: 7.5px; color: var(--muted); }
  .footer-nav .current { color: var(--red); font-weight: 700; }
  .copyright { position: absolute; left: 0; right: 0; top: 80px; font-size: 6.8px; color: var(--muted); }
  .copyright a { color: var(--red); }
</style>
</head>
<body>

<header class="site-header">
  <a class="brand" href="#"><span class="brand-dot"></span>Pitlane Ledger</a>
  <a class="nav-signup" href="#">SIGN UP</a>
  <a class="nav-login" href="#">LOG IN</a>
</header>

<section class="hero" role="img" aria-label="Black sports car cornering at speed on a race track">
  <h1 class="hero-title">LET US TRACK<br>YOUR PARTS</h1>
  <p class="hero-lead">Lorem ipsum dolor sit amet, consectetuer adipiscing elit, sed diam nonummy nibh</p>
  <a class="btn btn-light btn-pricing" href="#">Pricing</a>
  <a class="btn btn-red btn-register" href="#">Get Registered</a>
  <div class="hero-dots"><span></span><span></span><span class="active"></span><span></span><span></span></div>
</section>

<section class="intro">
  <h2 class="intro-heading">WHAT<br><span class="brand">Pitlane Ledger</span> DO ?</h2>
  <div class="intro-divider"></div>
  <p class="intro-text">Lorem ipsum dolor sit amet, consectetuer adipiscing elit, sed diam nonummy nibh euismod tincidunt ut laoreet dolore magna aliquam erat volutpat. Ut wisi enim ad minim veniam, quis nostrud exerci tation ullamcorper suscipit lobortis nisl ut aliquip ex ea commodo consequat.<br>Duis autem vel eum iriure dolor in hendrerit in vulputate velit esse molestie consequat, vel illum dolore eu feugiat nulla facilisis at vero eros et accumsan et iusto odio dignissim qui blandit praesent luptatum zzril delenit augue duis dolore te feugait nulla facilisi.</p>
</section>

<section class="feature feature-car">
  <div class="feature-photo" role="img" aria-label="Rear view of a white and red GT race car on track"></div>
  <h3 class="feature-title">Tracking the car <span class="ring"></span></h3>
  <p class="feature-text">Lorem ipsum dolor sit amet, consectetuer adipiscing elit, sed diam nonummy nibh euismod tincidunt ut laoreet dolore magna aliquam erat volutpat. Ut wisi enim ad minim veniam, quis nostrud exerci tation ullamcorper suscipit lobortis nisl ut aliquip ex ea commodo consequat.<br>Duis autem vel eum iriure dolor in hendrerit in vulputate velit esse molestie consequat, vel illum dolore eu feugiat .</p>
  <a class="btn btn-red" href="#">View Info</a>
</section>

<section class="feature feature-data">
  <div class="feature-photo" role="img" aria-label="Black GT race car with rear wing driving on a circuit"></div>
  <h3 class="feature-title"><span class="ring"></span> Data transfer</h3>
  <p class="feature-text">Duis autem vel eum iriure dolor in hendrerit in vulputate velit esse molestie consequat, vel illum dolore eu feugiat nulla facilisis at vero eros et accumsan et iusto odio dignissim qui blandit praesent luptatum zzril delenit augue duis dolore te feugait nulla facilisi.</p>
  <a class="btn btn-red" href="#">View Info</a>
</section>

<section class="feature feature-management">
  <div class="feature-photo" role="img" aria-label="Pit crew servicing a GT race car in the pit lane"></div>
  <h3 class="feature-title">Management <span class="ring"></span></h3>
  <p class="feature-text">Lorem ipsum dolor sit amet, consectetuer adipiscing elit, sed diam nonummy nibh euismod tincidunt ut laoreet dolore magna aliquam erat volutpat. Ut wisi enim ad minim veniam, quis nostrud exerci tation ullamcorper suscipit lobortis nisl ut aliquip ex ea commodo consequat.</p>
  <a class="btn btn-red" href="#">View Info</a>
</section>

<footer class="site-footer">
  <a class="brand" href="#"><span class="brand-dot"></span>Pitlane Ledger</a>
  <div class="social">
    <span class="social-item"><span class="social-btn">Like</span><span class="social-count">13k</span></span>
    <span class="social-item"><span class="social-btn follow">Follow</span><span class="social-count">13.2K followers</span></span>
  </div>
  <nav class="footer-nav">
    <a class="current" href="#">Home</a>
    <a href="#">Register</a>
    <a href="#">My Cars</a>
    <a href="#">Contact Us</a>
  </nav>
  <p class="copyright">Copyright 2014 Morlek BVBA. All rights reserved. <a href="#">Terms of Service</a> &amp; <a href="#">Privacy Policy</a>.</p>
</footer>

</body>
</html>
```